Hollybrook Hounds Jamboree Sponsor & Stallholder Leaflet Design

Hollybrook Hounds Jamboree is the updated and refreshed version of the Pemberly Canine Fete (See www.pemberlycaninefete.co.uk).
Under new management, we need a leaflet designed to promote the event to potential stallholders and sponsors.
Hollybrook Hounds Jamboree is a fun day out for dogs and their human companions, with a range of activities for both.
As this is an outdoor event, we would like this theme in the leaflet.
It is being held in the grounds of Thistlecombe Grange - http://www.thistlecombegrange.com
Note:
Leaflet format of DL/6 page is preferred, but will accept A5/4page
I will require the final work in InDesign format
Target Market(s)
Dog owners and lovers
Industry/Entity Type
Event
Look and feel
Each slider illustrates characteristics of the customer's brand and the style your logo design should communicate.

```html
<!DOCTYPE html>
<html lang="en">
<head>
<meta charset="utf-8">
<title>Hollybrook Hounds Jamboree – Sponsor &amp; Stallholder Leaflet</title>
<link rel="stylesheet" href="https://fonts.googleapis.com/css2?family=Fredoka:wght@600&family=Raleway:wght@400;600;700&family=Oswald:wght@400;500&display=swap">
<style>
  :root{
    --backdrop:#e4e5e4;
    --paper:#ffffff;
    --ink:#2b2b2b;
    --leaf:#2f8a2d;
    --forest:#0f4a20;
    --forest-deep:#0a3517;
    --rule:#3f8f45;
    --lime:#93d150;
    --white:#ffffff;
  }
  *{box-sizing:border-box;margin:0;padding:0}
  html,body{width:1200px;height:987px;overflow:hidden}
  body{background:var(--backdrop);position:relative;font-family:"Raleway",sans-serif;color:var(--ink)}

  .leaflet{position:absolute;left:21px;top:84px;width:1158px;height:820px;display:flex;box-shadow:0 6px 22px rgba(0,0,0,.18)}
  .panel{width:386px;height:820px;position:relative;overflow:hidden}

  /* Inside info panel */
  .panel--info{background:var(--paper);padding:26px 24px 20px}
  .panel--info p{font-size:11.3px;line-height:1.42;text-align:justify;margin-bottom:9px}
  .panel--info strong{font-weight:700}
  .section-title{font-family:"Fredoka",sans-serif;font-weight:600;color:var(--leaf);font-size:25px;text-align:center;line-height:1.05;margin:14px 0 12px}
  .promo{display:flex;justify-content:space-between;align-items:flex-end}
  .promo-list{list-style:none;font-size:11.5px;font-weight:700;line-height:1.75}
  .promo-list li{display:flex;align-items:center;gap:9px}
  .promo-list li::before{content:"";width:8px;height:8px;background:var(--leaf);flex:none}
  .puppy-photo{width:74px;height:90px;border-radius:10px;background:linear-gradient(180deg,#e9e4df,#5a3a24 45%,#3a2616)}

  /* Rates panel */
  .panel--rates{background:var(--forest);padding:22px 20px;color:var(--white)}
  .rates-title{font-family:"Oswald",sans-serif;font-weight:500;font-size:17px;letter-spacing:.06em;text-transform:uppercase;text-align:center;color:var(--lime);margin-bottom:12px}
  .rates-table{width:100%;border-collapse:collapse;font-size:11.5px}
  .rates-table th,.rates-table td{border:1px solid var(--rule);padding:7px 8px;text-align:left}
  .rates-table th{font-family:"Oswald",sans-serif;font-weight:400;color:var(--lime);letter-spacing:.04em}
  .rates-table .price{text-align:right;font-weight:600}
  .benefits-title{font-family:"Oswald",sans-serif;font-weight:500;font-size:15px;letter-spacing:.05em;text-transform:uppercase;color:var(--lime);margin:20px 0 10px;text-align:center}
  .benefits-table{width:100%;border-collapse:collapse;font-size:11px}
  .benefits-table th,.benefits-table td{border:1px solid var(--rule);height:44px;padding:4px 6px;text-align:center}
  .benefits-table th{font-family:"Oswald",sans-serif;font-weight:400;color:var(--lime);height:30px}
  .benefits-table td.benefit{text-align:left;width:42%}
  .tick{width:13px;height:13px;display:inline-block}

  /* Cover panel */
  .panel--cover{background:var(--forest-deep)}
  .cover-photo{position:absolute;inset:0 0 76px 0;background:linear-gradient(180deg,#0b3a18 0%,#154a1f 28%,#2b6a26 40%,#4f9a2e 48%,#58a333 75%,#4a9029 100%)}
  .cover-head{position:absolute;top:70px;left:20px;right:20px;text-align:center}
  .event-name{font-family:"Raleway",sans-serif;font-weight:700;color:var(--white);font-size:34px;line-height:1.15}
  .event-dates{font-family:"Oswald",sans-serif;font-weight:500;color:var(--white);font-size:23px;letter-spacing:.03em;margin-top:14px}
  .cover-band{position:absolute;left:0;right:0;bottom:0;height:100px}
  .cover-band svg{position:absolute;inset:0;width:100%;height:100%}
  .cover-band-text{position:absolute;left:0;right:0;bottom:26px;text-align:center;font-family:"Oswald",sans-serif;font-size:13.5px;letter-spacing:.08em;color:var(--lime);text-transform:uppercase}
</style>
</head>
<body>
<main class="leaflet">

  <section class="panel panel--info">
    <p><strong>Pemberly Canine Fete</strong> was created and launched in 2009, in aid of Aid for Veterans Trust, co-inciding with the deployment of the Eastmarch Rifles on active service overseas. Parents left behind during their deployment were amongst the committed volunteers who participated and helped in the organisation of the event. The event captured the animal loving spirit of Wexmoor at a point when the whole county was passionate in their support of 'our blokes doing their bit' overseas. Expecting a few hundred dogs and 5,000 humans, it actual attracted circa 3,000 dogs, with almost 15,000 guests; the inaugural event was seen as an outstanding success. 2010 saw a visitor increase of circa 20%.</p>
    <p>Due to the overwhelming footfall, 2013 will become a two day event and is now known as 'Hollybrook Hounds Jamboree'.</p>

    <h2 class="section-title">Where Is It Held?</h2>
    <p>Thistlecombe Grange is one of Wexmoor's most romantic and impressive large Edwardian country houses set in sweeping parkland. It was built to a grand design by Edwin Albert Harrowgate, grandson of Edwin Harrowgate, the inventor of modern holiday travel, and is lived in today by his descendants. Although a private family home, and not open to the public, Thistlecombe Grange offers a unique and magical venue for the Pemberly Canine Fete.</p>
    <p>Near Brackleigh, in North Wexmoor, Thistlecombe Grange is approximately 30 minutes from Castlebury.</p>

    <h2 class="section-title">Who Will Attend?</h2>
    <p>The target audience for this event is anyone who likes, owns or has an interest in dogs! Heavily promoted to dog lovers and owners, across several mediums it attracts visitors of all ages across the demographic spectrum.</p>

    <h2 class="section-title">How Will It<br>Be Promoted?</h2>
    <div class="promo">
      <ul class="promo-list">
        <li>Dedicated website</li>
        <li>Social Media - Pawbook, Chirper etc</li>
        <li>Regional Advertising</li>
        <li>Dog &amp; pet Press</li>
        <li>Regional Radio</li>
        <li>Regional database via email</li>
      </ul>
      <div class="puppy-photo" role="img" aria-label="Photo of a small brown puppy sitting"></div>
    </div>
  </section>

  <section class="panel panel--rates">
    <h2 class="rates-title">Sponsorship &amp; Stall Rates</h2>
    <table class="rates-table">
      <thead><tr><th>Package</th><th class="price">Price</th></tr></thead>
      <tbody>
        <tr><td>Headline</td><td class="price">£1,500</td></tr>
        <tr><td>Gold</td><td class="price">£750</td></tr>
        <tr><td>Silver</td><td class="price">£400</td></tr>
        <tr><td>Bronze</td><td class="price">£200</td></tr>
        <tr><td>Trade Stall</td><td class="price">£95</td></tr>
        <tr><td>Food Stall</td><td class="price">£75</td></tr>
      </tbody>
    </table>

    <h3 class="benefits-title">What You Receive</h3>
    <table class="benefits-table">
      <thead><tr><th></th><th>H</th><th>G</th><th>S</th><th>B</th></tr></thead>
      <tbody>
        <tr><td class="benefit">Logo on banners</td>
          <td><svg class="tick" viewBox="0 0 14 14"><path d="M2 7.5l3 3 7-7" fill="none" stroke="#93d150" stroke-width="2"/></svg></td>
          <td><svg class="tick" viewBox="0 0 14 14"><path d="M2 7.5l3 3 7-7" fill="none" stroke="#93d150" stroke-width="2"/></svg></td>
          <td></td><td></td></tr>
        <tr><td class="benefit">Website listing</td>
          <td><svg class="tick" viewBox="0 0 14 14"><path d="M2 7.5l3 3 7-7" fill="none" stroke="#93d150" stroke-width="2"/></svg></td>
          <td><svg class="tick" viewBox="0 0 14 14"><path d="M2 7.5l3 3 7-7" fill="none" stroke="#93d150" stroke-width="2"/></svg></td>
          <td><svg class="tick" viewBox="0 0 14 14"><path d="M2 7.5l3 3 7-7" fill="none" stroke="#93d150" stroke-width="2"/></svg></td>
          <td><svg class="tick" viewBox="0 0 14 14"><path d="M2 7.5l3 3 7-7" fill="none" stroke="#93d150" stroke-width="2"/></svg></td></tr>
        <tr><td class="benefit">Social media posts</td>
          <td><svg class="tick" viewBox="0 0 14 14"><path d="M2 7.5l3 3 7-7" fill="none" stroke="#93d150" stroke-width="2"/></svg></td>
          <td><svg class="tick" viewBox="0 0 14 14"><path d="M2 7.5l3 3 7-7" fill="none" stroke="#93d150" stroke-width="2"/></svg></td>
          <td><svg class="tick" viewBox="0 0 14 14"><path d="M2 7.5l3 3 7-7" fill="none" stroke="#93d150" stroke-width="2"/></svg></td>
          <td></td></tr>
        <tr><td class="benefit">Free entry passes</td>
          <td><svg class="tick" viewBox="0 0 14 14"><path d="M2 7.5l3 3 7-7" fill="none" stroke="#93d150" stroke-width="2"/></svg></td>
          <td><svg class="tick" viewBox="0 0 14 14"><path d="M2 7.5l3 3 7-7" fill="none" stroke="#93d150" stroke-width="2"/></svg></td>
          <td><svg class="tick" viewBox="0 0 14 14"><path d="M2 7.5l3 3 7-7" fill="none" stroke="#93d150" stroke-width="2"/></svg></td>
          <td><svg class="tick" viewBox="0 0 14 14"><path d="M2 7.5l3 3 7-7" fill="none" stroke="#93d150" stroke-width="2"/></svg></td></tr>
        <tr><td class="benefit">Programme advert</td>
          <td><svg class="tick" viewBox="0 0 14 14"><path d="M2 7.5l3 3 7-7" fill="none" stroke="#93d150" stroke-width="2"/></svg></td>
          <td></td><td></td><td></td></tr>
      </tbody>
    </table>
  </section>

  <section class="panel panel--cover">
    <div class="cover-photo" role="img" aria-label="Outdoor photo of a smiling woman sitting on the grass hugging a pale Labrador, dark green trees behind"></div>
    <header class="cover-head">
      <h1 class="event-name">Hollybrook Hounds<br>Jamboree</h1>
      <p class="event-dates">27TH &amp; 28TH JULY 2013</p>
    </header>
    <footer class="cover-band">
      <svg viewBox="0 0 386 100" preserveAspectRatio="none"><path d="M0 30 Q193 10 386 22 L386 100 L0 100Z" fill="#0f4a20"/><path d="M0 30 Q193 10 386 22" fill="none" stroke="#2f8a2d" stroke-width="2"/></svg>
      <p class="cover-band-text">Sponsorship &amp; Trade Exhibitor Opportunities</p>
    </footer>
  </section>

</main>
</body>
</html>
```